Business Card- Occupational Therapist

I need business cards for Bright Harbour KidMotion, I am an Occupational Therapist offering child centred play therapy.
I am a sole private practitioner offering play therapy services to families in rural Great Southern region of WA, my mission statement is "helping rural children and communities thrive"
This is a new business so I am needing to promote the value of child centred play therapy within the community, and my referrers (target audience) will be: rural GPs (doctors), child health nurse, schools, disability providers, child protection workers etc) but also the families of young children in rural areas.
Target Market(s)
Families of children
Referrers (Doctors, child health nurse, schools, disability providers, child protection workers)
Industry/Entity Type
Mental Health
Contact Information for Business Card
Maren Koltwick
Occupational Therapist
Phone: 0471 828 305
Email: maren@bhkidmotion.com.au
PO Box 71 | WARRENDALE WA 6412
Requirements
Must have
- Include Bright Harbour KidMotion logo and my contact details.
Include my credentials as an Occupational Therapist and Child Centred Play Therapist
Nice to have
- "Play is a child's language and toys are their words" Dorian Welkmore

```html
<!DOCTYPE html>
<html lang="en">
<head>
<meta charset="utf-8">
<title>Bright Harbour KidMotion – Business Card</title>
<link href="https://fonts.googleapis.com/css2?family=Quicksand:wght@400;500&family=Roboto:wght@400;700&display=swap" rel="stylesheet">
<style>
  :root {
    --backdrop: #262626;
    --card: #171717;
    --pattern: #232323;
    --pattern-edge: #1b1b1b;
    --green: #2e9e2f;
    --purple: #7b2a80;
    --text: #f2f2f2;
  }
  * { margin: 0; padding: 0; box-sizing: border-box; }
  html, body {
    width: 1138px;
    height: 1200px;
    overflow: hidden;
    background: var(--backdrop);
  }
  .canvas { position: relative; width: 1138px; height: 1200px; }
  .card {
    position: absolute;
    top: 276px;
    width: 374px;
    height: 620px;
    background: var(--card);
    border-radius: 11px;
    overflow: hidden;
    color: var(--text);
    text-align: center;
  }
  .card--front { left: 156px; }
  .card--back { left: 578px; }

  .brand-name {
    position: absolute;
    left: 0; right: 0;
    font-family: "Quicksand", sans-serif;
    font-weight: 400;
    font-size: 31px;
    line-height: 36px;
    color: var(--text);
  }
  .card--front .brand-name { top: 50px; }
  .card--back .brand-name { top: 184px; }

  .brand-mark {
    position: absolute;
    left: 50%;
    width: 34px;
    height: 34px;
    margin-left: -17px;
    border-radius: 50%;
    background: var(--green);
  }
  .card--front .brand-mark { top: 184px; }
  .card--back .brand-mark { top: 330px; }

  .holder-name {
    position: absolute;
    top: 340px; left: 0; right: 0;
    font-family: "Roboto", sans-serif;
    font-weight: 700;
    font-size: 24px;
    color: var(--green);
  }
  .holder-role {
    position: absolute;
    top: 373px; left: 0; right: 0;
    font-family: "Roboto", sans-serif;
    font-size: 16px;
  }
  .contact-divider {
    position: absolute;
    top: 412px; left: 60px; right: 60px;
    height: 28px;
    display: flex;
    align-items: center;
    justify-content: center;
    gap: 4px;
  }
  .contact-divider .rule {
    flex: 1;
    height: 2px;
    background: linear-gradient(to right, transparent, var(--purple));
  }
  .contact-divider .rule--right { background: linear-gradient(to left, transparent, var(--purple)); margin-left: 10px; }
  .contact-divider .rule--left { margin-right: 10px; }
  .contact-icon { width: 27px; height: 27px; }

  .contact-list {
    position: absolute;
    top: 452px; left: 0; right: 0;
    font-family: "Roboto", sans-serif;
    font-size: 16px;
    line-height: 24px;
    list-style: none;
  }
  .postal {
    position: absolute;
    top: 543px; left: 0; right: 0;
    font-family: "Roboto", sans-serif;
    font-size: 16px;
  }
  .back-pattern {
    position: absolute;
    inset: 0;
    background: radial-gradient(circle at 50% 45%, var(--pattern-edge) 0%, var(--pattern) 100%);
  }
</style>
</head>
<body>
<div class="canvas">

  <section class="card card--front">
    <h1 class="brand-name">Bright Harbour<br>KidMotion</h1>
    <div class="brand-mark"></div>

    <p class="holder-name">Maren Koltwick</p>
    <p class="holder-role">Occupational Therapist</p>

    <div class="contact-divider">
      <span class="rule rule--left"></span>
      <svg class="contact-icon" viewBox="0 0 28 28" aria-label="phone">
        <circle cx="14" cy="14" r="12.5" fill="none" stroke="var(--purple)" stroke-width="2"/>
        <path d="M8 11 q6 -5 12 0 l-1.5 2 h-2 v-1.5 h-5 v1.5 h-2 z M9.5 14 h9 l1 5 h-11 z" fill="var(--purple)"/>
      </svg>
      <svg class="contact-icon" viewBox="0 0 28 28" aria-label="email">
        <circle cx="14" cy="14" r="12.5" fill="none" stroke="var(--purple)" stroke-width="2"/>
        <rect x="7.5" y="9.5" width="13" height="9" fill="var(--purple)"/>
        <path d="M7.5 9.5 L14 15 L20.5 9.5" fill="none" stroke="var(--card)" stroke-width="1.2"/>
      </svg>
      <svg class="contact-icon" viewBox="0 0 28 28" aria-label="website">
        <circle cx="14" cy="14" r="12.5" fill="none" stroke="var(--purple)" stroke-width="2"/>
        <circle cx="14" cy="14" r="6.5" fill="none" stroke="var(--purple)" stroke-width="1.4"/>
        <ellipse cx="14" cy="14" rx="2.8" ry="6.5" fill="none" stroke="var(--purple)" stroke-width="1.2"/>
        <path d="M7.5 14 h13 M8.5 11 h11 M8.5 17 h11" stroke="var(--purple)" stroke-width="1"/>
      </svg>
      <span class="rule rule--right"></span>
    </div>

    <ul class="contact-list">
      <li>0471 828 305</li>
      <li>maren@bhkidmotion.com.au</li>
      <li>www.bhkidmotion.com.au</li>
    </ul>
    <p class="postal">PO Box 71 | WARRENDALE WA 6412</p>
  </section>

  <section class="card card--back">
    <div class="back-pattern" role="img" aria-label="Faint repeating brand pattern across the card back"></div>
    <h2 class="brand-name">Bright Harbour<br>KidMotion</h2>
    <div class="brand-mark"></div>
  </section>

</div>
</body>
</html>
```